ZOVA Framework. the way you communicate in every situation and in all environments.

I would like you to create a diagram depicting a very specific process of communication. it must follow the look of the diagram that i have attached. this is going to be used in a book called BEDROCK. it is going to explain the fact that we communicate all the same way using this process as we communicate. it starts with the fact that everyone takes everything that is said personally and then moves on to filters, which is your own agenda or experience kicking in. then you move to your why it matters, which is your motivation and ends with the choice of words you use when you communicate. if you are going to be successful then you must separate the person from the issue.

Target Market(s)

market is executive business people around the world

Industry/Entity Type

Consulting

Font styles to use
Sans Serif

Colors

Designer to choose only greyscale colors for use in the design.

Requirements
Must have
• I would like it to have a diving/ocean/snorkel feel to it. The analogy we are using is to make a deep dive when you are communicating. it must have every part of the diagram you see, it starts at the top with the zova framework (and the words) it then connects to the filters which connects to the why it matters with connects to the words and then end with the separating the person from the issue.
Nice to have
• we are writing a black and white book NO color. therefore the words should be clear and easy to read. Each section should be able to stand on its own so we can write about it separately.
Should not have
• the diagram DOES NOT have to look like the one i gave you. it must explain the fact that it starts with ZOVA and ends with Separate and must pass through the three areas to get to the SEPARATE.

```html
<!DOCTYPE html>
<html lang="en">
<head>
<meta charset="utf-8">
<title>ZOVA Framework – Communication Diagram</title>
<link rel="stylesheet" href="https://fonts.googleapis.com/css2?family=Montserrat:ital,wght@0,600;0,700;1,600;1,700&display=swap">
<style>
  :root {
    --ring-grey: #4a4a4a;
    --core-grey: #3a3a3a;
    --note-grey: #2e2e2e;
    --label-white: #ffffff;
    --water-light: #f1f1f1;
    --water-mid: #e2e2e2;
    --bubble-grey: #9a9a9a;
    --paper: #ffffff;
  }
  html, body {
    margin: 0;
    padding: 0;
    width: 1200px;
    height: 1117px;
    overflow: hidden;
    background: var(--paper);
  }
  .diagram {
    display: block;
    width: 1200px;
    height: 1117px;
  }
  .surface-wave {
    fill: none;
    stroke: var(--water-mid);
    stroke-width: 3;
    stroke-linecap: round;
  }
  .surface-wave.soft { stroke: var(--water-light); stroke-width: 2; }
  .bubble {
    fill: none;
    stroke: var(--bubble-grey);
    stroke-width: 2;
  }
  .stage-ring-dashed {
    fill: none;
    stroke: var(--ring-grey);
    stroke-width: 3;
    stroke-dasharray: 6 5;
  }
  .stage-ring-solid {
    fill: none;
    stroke: var(--ring-grey);
    stroke-width: 4;
  }
  .stage-core { fill: var(--core-grey); }
  .stage-label {
    font-family: "Montserrat", sans-serif;
    font-weight: 600;
    font-size: 22px;
    letter-spacing: 0.8px;
    fill: var(--label-white);
    text-anchor: middle;
  }
  .connector {
    stroke: var(--ring-grey);
    stroke-width: 3;
  }
  .connector-dot { fill: var(--ring-grey); }
  .chevron {
    fill: none;
    stroke: var(--ring-grey);
    stroke-width: 4;
    stroke-linecap: round;
    stroke-linejoin: round;
  }
  .stage-note {
    font-family: "Montserrat", sans-serif;
    font-style: italic;
    font-weight: 600;
    font-size: 15px;
    fill: var(--note-grey);
  }
  .stage-note.centered { text-anchor: middle; }
</style>
</head>
<body>
<svg class="diagram" viewBox="0 0 1140 1060" preserveAspectRatio="none" role="img" aria-label="ZOVA Framework communication process diagram">

  <!-- Water surface -->
  <g class="water-surface">
    <path class="surface-wave" d="M80 150 q40 -18 80 0 t80 0 t80 0 t80 0 t80 0 t80 0 t80 0 t80 0 t80 0 t80 0 t80 0 t80 0"/>
    <path class="surface-wave soft" d="M40 172 q40 -14 80 0 t80 0 t80 0 t80 0 t80 0 t80 0 t80 0 t80 0 t80 0 t80 0 t80 0 t80 0 t80 0"/>
  </g>

  <!-- Rising bubbles -->
  <g class="bubbles">
    <circle class="bubble" cx="238" cy="220" r="5"/>
    <circle class="bubble" cx="252" cy="200" r="3.5"/>
    <circle class="bubble" cx="226" cy="192" r="2.5"/>
    <circle class="bubble" cx="230" cy="505" r="4"/>
    <circle class="bubble" cx="244" cy="490" r="2.5"/>
    <circle class="bubble" cx="756" cy="790" r="4"/>
    <circle class="bubble" cx="768" cy="772" r="2.5"/>
  </g>

  <!-- Connectors -->
  <g class="connectors">
    <line class="connector" x1="193" y1="446" x2="193" y2="487"/>
    <circle class="connector-dot" cx="193" cy="487" r="8"/>
    <line class="connector" x1="296" y1="645" x2="336" y2="645"/>
    <circle class="connector-dot" cx="336" cy="645" r="8"/>
    <line class="connector" x1="558" y1="645" x2="596" y2="645"/>
    <circle class="connector-dot" cx="596" cy="645" r="8"/>
    <line class="connector" x1="713" y1="743" x2="713" y2="785"/>
    <circle class="connector-dot" cx="713" cy="785" r="8"/>
  </g>

  <!-- Stage: ZOVA Framework -->
  <g class="stage stage-framework">
    <circle class="stage-ring-dashed" cx="193" cy="348" r="100"/>
    <circle class="stage-ring-solid" cx="193" cy="348" r="100" stroke-dasharray="340 400" transform="rotate(60 193 348)"/>
    <circle class="stage-core" cx="193" cy="348" r="90"/>
    <text class="stage-label" x="193" y="338">ZOVA</text>
    <text class="stage-label" x="193" y="366">Framework</text>
  </g>
  <path class="chevron" d="M313 336 l10 12 l-10 12 M327 336 l10 12 l-10 12"/>
  <text class="stage-note" x="360" y="332">When words are taken</text>
  <text class="stage-note" x="360" y="352">personally, what</text>
  <text class="stage-note" x="360" y="372">happens?</text>

  <!-- Stage: Your Filters -->
  <g class="stage stage-filters">
    <circle class="stage-ring-dashed" cx="197" cy="645" r="100"/>
    <circle class="stage-ring-solid" cx="197" cy="645" r="100" stroke-dasharray="366 400" transform="rotate(180 197 645)"/>
    <circle class="stage-core" cx="197" cy="645" r="90"/>
    <text class="stage-label" x="197" y="637">Your</text>
    <text class="stage-label" x="197" y="665">Filters</text>
  </g>
  <path class="chevron" d="M186 768 l11 9 l11 -9 M186 781 l11 9 l11 -9"/>
  <text class="stage-note centered" x="197" y="836">An accumulation of</text>
  <text class="stage-note centered" x="197" y="856">your experience,</text>
  <text class="stage-note centered" x="197" y="876">knoweldge and values</text>

  <!-- Stage: Why It Matters -->
  <g class="stage stage-why">
    <circle class="stage-ring-dashed" cx="460" cy="645" r="100"/>
    <circle class="stage-ring-solid" cx="460" cy="645" r="100" stroke-dasharray="314 400" transform="rotate(-20 460 645)"/>
    <circle class="stage-core" cx="460" cy="645" r="90"/>
    <text class="stage-label" x="460" y="637">Why It</text>
    <text class="stage-label" x="460" y="665">Matters</text>
  </g>
  <path class="chevron" d="M449 768 l11 9 l11 -9 M449 781 l11 9 l11 -9"/>
  <text class="stage-note centered" x="458" y="836">This is your compass.</text>
  <text class="stage-note centered" x="458" y="856">It is what motivattes</text>
  <text class="stage-note centered" x="458" y="876">you, what drive you.</text>

  <!-- Stage: Your Words -->
  <g class="stage stage-words">
    <circle class="stage-ring-dashed" cx="713" cy="645" r="100"/>
    <circle class="stage-ring-solid" cx="713" cy="645" r="100" stroke-dasharray="350 400" transform="rotate(150 713 645)"/>
    <circle class="stage-core" cx="713" cy="645" r="90"/>
    <text class="stage-label" x="713" y="637">Your</text>
    <text class="stage-label" x="713" y="665">Words</text>
  </g>
  <path class="chevron" d="M836 633 l10 12 l-10 12 M850 633 l10 12 l-10 12"/>
  <text class="stage-note" x="890" y="628">This is your immediate</text>
  <text class="stage-note" x="890" y="648">response, verbal or</text>
  <text class="stage-note" x="890" y="668">perhaps non-verbal</text>

  <!-- Stage: What To Do -->
  <g class="stage stage-action">
    <circle class="stage-ring-dashed" cx="718" cy="915" r="100"/>
    <circle class="stage-ring-solid" cx="718" cy="915" r="100" stroke-dasharray="350 400" transform="rotate(-60 718 915)"/>
    <circle class="stage-core" cx="718" cy="915" r="90"/>
    <text class="stage-label" x="718" y="910">What To</text>
    <text class="stage-label" x="718" y="938">Do</text>
  </g>
  <path class="chevron" d="M840 891 l10 12 l-10 12 M854 891 l10 12 l-10 12"/>
  <text class="stage-note" x="898" y="899">Separate the Person</text>
  <text class="stage-note" x="898" y="919">from the Issue</text>

</svg>
</body>
</html>
```